Emergency Vehicle Installer and Security Firm Needs a Business Card

Our company "Corvalt" need a business card for our Emergency Vehicle Equipment Installation and Infrastructure Security Business. We are contract designers, manufacturers and installers for Emergency Vehicle Fleets. This includes installation of Emergency Lights, Sirens, Vehicle Graphics and Radio Communications. We also supply this products to an international market. We also do consultant, and installation of high level security access, alarm and surveillance equipment for medium to large size businesses.

The design should represent a level of trust in our professionalism and expertise. It should visually display our ongoing relationship with the emergency services, but not overtake our commitment to high level security options.

Target Market(s)

Emergency Services and Businesses requiring high level security

Industry/Entity Type

Business

Contact Information for Business Card

*note complete details will be given to the winning designer for revising. The name "Mark Pell will be used to fill in name".

Mark Pell
Managing Director
Corvalt NZ Limited
Phone: +64 027 604 91352
Email: mark.pell@corvalt-example.co.nz

Requirements
Must have
• Card must be in black. Using our logo on the top as supplied. Designers should try having the reverse side as a blurred image of police lights (red and blue) with our logo in greyscale in the centre (this is not particularly a requirement, but feel free to play around with this option).
Nice to have
• A card design that looks good when spot UV printed. A clean compact and graphic design. A grey scale feel on the front (excluding logo, but you can play around with that idea). Rounded smooth text.
Should not have
• Will update this section as designs come through - feel free to submit what you feel would look good.

```html
<!DOCTYPE html>
<html lang="en">
<head>
<meta charset="utf-8">
<title>Corvalt Business Card</title>
<link rel="stylesheet" href="https://fonts.googleapis.com/css2?family=Lato:wght@400;700;900&display=swap">
<style>
  :root {
    --backdrop: #8f8f8f;
    --card-black: #151515;
    --card-charcoal: #2a2a2a;
    --text-white: #f2f2f2;
    --text-grey: #b9b9b9;
    --accent-red: #e0202a;
    --rule-grey: #5a5a5a;
    --light-red: #e3162f;
    --light-blue: #3a4fd8;
    --night: #0d0a1c;
  }
  * { margin: 0; padding: 0; box-sizing: border-box; }
  html, body {
    width: 1200px; height: 926px; overflow: hidden;
    background: var(--backdrop);
    font-family: "Lato", sans-serif;
  }
  .canvas {
    width: 1200px; height: 926px;
    display: flex; flex-direction: column; align-items: center; justify-content: center;
    gap: 40px;
  }
  .card {
    position: relative;
    width: 720px; height: 411px;
    overflow: hidden;
    box-shadow: 0 10px 30px rgba(0,0,0,0.35);
  }

  /* Reverse side */
  .card-back { background: var(--night); }
  .lights-photo {
    position: absolute; inset: 0;
    background:
      radial-gradient(ellipse 34% 46% at 66% 52%, rgba(255,60,70,0.95), rgba(227,22,47,0.55) 45%, transparent 75%),
      radial-gradient(ellipse 22% 26% at 20% 48%, rgba(120,140,255,0.9), rgba(58,79,216,0.5) 50%, transparent 80%),
      linear-gradient(160deg, #1b1240 0%, #2a0c2a 45%, #4a0a1c 75%, #1a0610 100%);
  }
  .back-brand {
    position: absolute; inset: 0;
    display: flex; align-items: center; justify-content: center; gap: 14px;
  }
  .brand-name {
    font-weight: 900; letter-spacing: 2px; text-transform: uppercase;
    color: var(--text-white);
  }
  .back-brand .brand-name { font-size: 70px; }
  .brand-dot {
    width: 18px; height: 18px; border-radius: 50%;
    background: var(--text-white);
  }

  /* Front side */
  .card-front {
    background:
      radial-gradient(ellipse 60% 55% at 35% 30%, #2e2e2e, transparent 75%),
      radial-gradient(ellipse 50% 50% at 80% 70%, #242424, transparent 80%),
      var(--card-black);
  }
  .front-brand {
    position: absolute; left: 40px; top: 34px;
    display: flex; align-items: center; gap: 10px;
  }
  .front-brand .brand-name { font-size: 46px; }
  .front-brand .brand-dot { width: 14px; height: 14px; background: var(--accent-red); }

  .contact-block {
    position: absolute; left: 34px; right: 34px; bottom: 52px;
  }
  .name-row {
    display: flex; justify-content: flex-end; align-items: baseline; gap: 8px;
  }
  .person-name {
    font-size: 27px; font-weight: 400; color: var(--text-grey); text-transform: uppercase;
  }
  .person-title {
    font-size: 15px; font-weight: 700; color: var(--accent-red); text-transform: uppercase;
  }
  .details-row {
    display: flex; align-items: baseline; margin-top: 8px;
    font-size: 16px; color: var(--text-white);
  }
  .company-name { color: var(--text-grey); font-size: 15px; margin-right: auto; }
  .detail { margin-left: 28px; }
  .detail-label { color: var(--accent-red); margin-right: 5px; }
  .rule {
    position: absolute; left: 34px; right: 34px; bottom: 34px;
    height: 1px; background: var(--rule-grey);
  }
</style>
</head>
<body>
<main class="canvas">
  <section class="card card-back" aria-label="Card reverse">
    <div class="lights-photo" role="img" aria-label="Blurred photograph of red and blue emergency vehicle lights at night"></div>
    <div class="back-brand">
      <span class="brand-name">Corvalt</span>
      <span class="brand-dot"></span>
    </div>
  </section>

  <section class="card card-front" aria-label="Card front">
    <div class="front-brand">
      <span class="brand-name">Corvalt</span>
      <span class="brand-dot"></span>
    </div>
    <div class="contact-block">
      <div class="name-row">
        <span class="person-name">Mark Pell</span>
        <span class="person-title">- Managing Director</span>
      </div>
      <div class="details-row">
        <span class="company-name">Corvalt NZ Limited</span>
        <span class="detail"><span class="detail-label">P:</span>+64 027 604 91352</span>
        <span class="detail"><span class="detail-label">E:</span>mark.pell@corvalt-example.co.nz</span>
      </div>
    </div>
    <div class="rule"></div>
  </section>
</main>
</body>
</html>
```